Flu Brochure- brief and easy-to-read

A team of health educators is looking to design a brochure on what Americans need to "know and do" when it comes to flu season. All copy and images will be provided.

The brochure needs to be an 8.5 x 11 inch bi-fold design.

I am only able to upload up to 5 files. So, additional images will have to sent via dropbox or some other mechanism.

Target Market(s)

The audience is vast, but the content and design need to be simple and engaging.

Industry/Entity Type

Health

Requirements
Must have
• Must Have:
- Clear and Simple, Easy-to-read and Understand and Act on- should be very focused on what the consumer should do about taking care of themselves when it comes to the flu.

We will provide all of the copy for the brochure design. We will also provide photographs for the project.

Captions for photographs that support the key message.

Should Not Have:
- x reverse print- e.g., no white font on a black background
x fancy fonts or heavy use of italics
x use of all capitals
x no full justification
x no use of drop caps

Must be multicultural as well.

```html
<!DOCTYPE html>
<html lang="en">
<head>
<meta charset="utf-8">
<title>Know and Do in Flu Season</title>
<link href="https://fonts.googleapis.com/css2?family=Anton&family=Oswald:wght@500;600;700&family=Roboto+Condensed:wght@400;700&family=Montserrat:wght@400&display=swap" rel="stylesheet">
<style>
  :root{
    --ink:#000;
    --sky:#29a8e0;
    --navy:#26348f;
    --paper:#fff;
    --fold:#b9b9b9;
  }
  html,body{margin:0;padding:0;overflow:hidden;background:var(--paper);}
  .brochure{position:relative;width:1200px;height:1085px;overflow:hidden;background:var(--paper);font-family:"Roboto Condensed",Arial,sans-serif;color:var(--ink);}
  .fold-line{position:absolute;left:600px;top:0;height:1085px;border-left:2px dashed var(--fold);}

  /* back panel */
  .recovery-title{position:absolute;left:16px;top:101px;margin:0;font-family:"Anton",Impact,sans-serif;font-weight:400;font-size:80px;line-height:84px;letter-spacing:2px;white-space:nowrap;}
  .recovery-tips{position:absolute;left:38px;top:268px;margin:0;padding:0 0 0 18px;color:var(--navy);font-size:18px;line-height:21px;width:425px;}
  .recovery-tips strong{font-weight:700;}
  .photo-children{position:absolute;left:45px;top:383px;width:533px;height:479px;background:radial-gradient(ellipse at 50% 50%,#e8d2b4 0%,#f3e6d6 45%,#fff 80%);}
  .resource-box{position:absolute;left:12px;top:862px;width:566px;height:131px;background:var(--sky);color:var(--paper);text-align:center;font-size:21px;line-height:27px;padding-top:10px;box-sizing:border-box;}
  .resource-box b{font-weight:700;}

  /* cover panel */
  .cover-know{position:absolute;left:605px;top:106px;font-family:"Anton",Impact,sans-serif;font-size:83px;line-height:83px;transform:scaleX(1.49);transform-origin:0 0;}
  .cover-and{position:absolute;left:634px;top:340px;transform:rotate(-90deg);transform-origin:0 0;font-family:"Oswald",sans-serif;font-weight:600;font-size:64px;line-height:56px;color:var(--navy);white-space:nowrap;}
  .cover-do{position:absolute;left:690px;top:180px;font-family:"Anton",Impact,sans-serif;font-size:170px;line-height:170px;transform:scaleX(1.41);transform-origin:0 0;}
  .cover-season{position:absolute;left:916px;top:298px;font-family:"Oswald",sans-serif;font-weight:600;font-size:44px;line-height:50px;letter-spacing:1px;color:var(--sky);white-space:nowrap;}
  .sponsor-label{position:absolute;left:1080px;top:110px;transform:rotate(14deg);font-family:"Oswald",sans-serif;font-size:14px;}
  .sponsor-name{position:absolute;left:982px;top:178px;font-family:"Roboto Condensed",sans-serif;font-size:26px;}
  .four-things{position:absolute;left:612px;top:356px;margin:0;font-family:"Anton",Impact,sans-serif;font-weight:400;font-size:25px;line-height:35px;letter-spacing:3.4px;white-space:nowrap;}
  .four-things span{color:var(--navy);}
  .pointer{position:absolute;left:612px;top:497px;}
  .steps{position:absolute;left:918px;top:346px;margin:0;padding:0;list-style:none;font-family:"Oswald",sans-serif;font-weight:700;font-size:72px;line-height:63px;color:var(--sky);}
  .photo-patient{position:absolute;left:612px;top:522px;width:224px;height:356px;background:linear-gradient(160deg,#dfe7df 0%,#c9b8a4 45%,#8a8f9c 100%);}
  .facts-know{position:absolute;left:875px;top:590px;font-family:"Oswald",sans-serif;font-weight:700;font-size:97px;line-height:97px;color:var(--navy);transform:scaleX(1.16);transform-origin:0 0;}
  .facts-sub{position:absolute;left:900px;top:694px;font-family:"Montserrat",sans-serif;font-size:52px;line-height:60px;}
  .facts-list{position:absolute;left:858px;top:764px;margin:0;padding:0 0 0 18px;width:292px;font-size:13.5px;line-height:20px;}
  .credits{position:absolute;left:733px;top:950px;width:370px;margin:0;text-align:center;font-size:7.5px;line-height:10px;font-style:italic;}
</style>
</head>
<body>
<div class="brochure">
  <div class="fold-line"></div>

  <section class="panel-back">
    <h2 class="recovery-title">ONCE YOU START<br>FEELING BETTER...</h2>
    <ol class="recovery-tips">
      <li>You still want to make sure you <strong>DON’T</strong> get other people sick.</li>
      <li>Stay home until you are <strong>“FEVER FREE”</strong> for at least 24 hours without the help of medicine.</li>
    </ol>
    <div class="photo-children" role="img" aria-label="Photo of four laughing children leaning toward the camera"></div>
    <div class="resource-box">
      For reliable information on flu:<br>
      <b>Call your doctor.</b><br>
      <b>Go to</b> http://www.flusmart.org/flu/<br>
      <b>Call</b> 1-800-FLU-SMRT (1-800-358-7678)
    </div>
  </section>

  <section class="panel-cover">
    <div class="cover-know">KNOW</div>
    <div class="cover-and">and</div>
    <div class="cover-do">DO</div>
    <div class="cover-season">in flu season</div>
    <div class="sponsor-label">Sponsored by:</div>
    <div class="sponsor-name">LOGO goes here</div>

    <h3 class="four-things"><span>FOUR</span> THINGS YOU CAN<br>DO TO PREPARE FOR<br>FLU SEASON AND KEEP<br>YOUR FAMILY HEALTHY</h3>
    <svg class="pointer" width="300" height="20" viewBox="0 0 300 20" aria-hidden="true">
      <line x1="0" y1="10" x2="290" y2="10" stroke="#000" stroke-width="2" stroke-dasharray="12 8"/>
      <polyline points="282,3 292,10 282,17" fill="none" stroke="#000" stroke-width="2"/>
    </svg>
    <ul class="steps">
      <li>KNOW</li>
      <li>PREVENT</li>
      <li>PROTECT</li>
      <li>TREAT</li>
    </ul>

    <div class="photo-patient" role="img" aria-label="Photo of a woman with a cold wrapped in a blanket, holding a tissue and a thermometer"></div>
    <div class="facts-know">KNOW</div>
    <div class="facts-sub">the facts:</div>
    <ol class="facts-list">
      <li>The flu is a virus.</li>
      <li>If you get the flu, you may not feel that bad, but sometimes the flu can make you so sick you can die.</li>
      <li>You catch the flu from other people.</li>
      <li>People with flu spread it by coughing, sneezing,<br>or spreading their germs.</li>
    </ol>
    <p class="credits">© 2013. Riverside Health Literacy Team, Riverside University.<br>Adams J, Brooks L, Carter M. Content based on scientific evidence<br>from national public health agencies as of March 2013.</p>
  </section>
</div>
</body>
</html>
```